Tech Startup Needs Business Card Design

I am looking for an eye catching business card design for our new company, Torn Kite. We are a place for business owners and contractors to share their experiences with their customers and check their current customers. Our website, www.torn-kite.co, may be able to offer some guidance as to the design.

Industry/Entity Type

Business

Contact Information for Business Card

Owen Barthwick
888-417-3083
Owen@torn-kite.co
www.torn-kite.co

```html
<!DOCTYPE html>
<html lang="en">
<head>
<meta charset="utf-8">
<title>Torn Kite — Business Card</title>
<link rel="stylesheet" href="https://fonts.googleapis.com/css2?family=Quicksand:wght@500;700&family=Varela+Round&display=swap">
<style>
  :root {
    --backdrop: #e6e6e6;
    --card: #ffffff;
    --ink: #1a1a1a;
    --brand-red: #e0282a;
    --brand-red-deep: #c81a1c;
    --brand-green: #1f8a2c;
    --bubble-green: #bcd94a;
    --highlight-red: #e8322c;
    --highlight-green: #2e9a3c;
  }
  * { box-sizing: border-box; margin: 0; padding: 0; }
  html, body {
    width: 1200px; height: 665px; overflow: hidden;
    background: var(--backdrop);
  }
  .stage {
    position: relative; width: 1200px; height: 665px;
    display: flex; align-items: center; justify-content: center; gap: 60px;
  }
  .card {
    position: relative; width: 500px; height: 290px;
    background: var(--card); overflow: hidden;
    box-shadow: 0 12px 28px rgba(0,0,0,0.18);
  }

  /* Shared wordmark */
  .wordmark {
    position: absolute; display: flex; align-items: center; gap: 10px;
    font-family: "Quicksand", sans-serif; font-weight: 700; color: var(--ink);
    letter-spacing: -0.5px; white-space: nowrap;
  }
  .wordmark .dot {
    width: 26px; height: 26px; border-radius: 50%; background: var(--brand-red);
  }

  /* Front */
  .front .wordmark { left: 30px; top: 34px; font-size: 44px; }
  .holder-name {
    position: absolute; left: 34px; top: 118px;
    font-family: "Quicksand", sans-serif; font-weight: 700;
    font-size: 30px; color: var(--brand-green); white-space: nowrap;
  }
  .contact-band {
    position: absolute; left: 0; top: 178px; width: 330px; height: 92px;
    background: linear-gradient(90deg, var(--brand-red-deep), var(--brand-red));
    border-radius: 0 46px 46px 0;
    display: flex; flex-direction: column; justify-content: center; align-items: flex-end;
    gap: 10px; padding-right: 22px;
  }
  .contact-line {
    display: flex; align-items: center; gap: 10px;
    font-family: "Quicksand", sans-serif; font-weight: 700;
    font-size: 17px; color: #fff; white-space: nowrap;
  }
  .contact-icon { width: 20px; height: 20px; }

  /* Back */
  .speech-bubble {
    position: absolute; left: 22px; top: 30px; width: 300px; height: 160px;
  }
  .speech-text {
    position: absolute; left: 44px; top: 62px; width: 260px;
    font-family: "Varela Round", sans-serif; font-size: 16px; line-height: 1.35;
    font-weight: 700; color: var(--ink); text-align: center;
    -webkit-text-stroke: 0.4px var(--ink);
  }
  .speech-text .warn { color: var(--highlight-red); -webkit-text-stroke-color: var(--highlight-red); }
  .speech-text .good { color: var(--highlight-green); -webkit-text-stroke-color: var(--highlight-green); }
  .character-art {
    position: absolute; right: 26px; top: 22px; width: 130px; height: 150px;
    border-radius: 10px;
    background: linear-gradient(160deg, #d9553f 0%, #7d8ea6 50%, #3d4c6b 100%);
    opacity: 0.85;
  }
  .back .wordmark { left: 30px; top: 212px; font-size: 42px; }
</style>
</head>
<body>
  <main class="stage">
    <section class="card front">
      <div class="wordmark"><span class="dot"></span>Torn Kite</div>
      <h1 class="holder-name">Owen Barthwick</h1>
      <div class="contact-band">
        <p class="contact-line">888-417-3083
          <svg class="contact-icon" viewBox="0 0 20 20"><circle cx="10" cy="10" r="9" fill="none" stroke="#fff" stroke-width="1.6"/><path d="M7 6.2l1.4-.4 1 2.2-.9.8a5 5 0 0 0 2.7 2.7l.8-.9 2.2 1-.4 1.4c-3.6.3-7.1-3.2-6.8-6.8z" fill="#fff"/></svg>
        </p>
        <p class="contact-line">Owen@torn-kite.co
          <svg class="contact-icon" viewBox="0 0 20 20"><circle cx="10" cy="10" r="9" fill="none" stroke="#fff" stroke-width="1.6"/><rect x="5.5" y="7" width="9" height="6.5" rx="1" fill="none" stroke="#fff" stroke-width="1.3"/><path d="M5.8 7.4L10 10.6l4.2-3.2" fill="none" stroke="#fff" stroke-width="1.3"/></svg>
        </p>
      </div>
    </section>

    <section class="card back">
      <svg class="speech-bubble" viewBox="0 0 300 160">
        <path d="M70 6h150c40 0 60 22 60 52v4l20 24-22-6c-6 40-30 74-70 74H70C30 154 6 124 6 80S30 6 70 6z" fill="var(--bubble-green)"/>
      </svg>
      <p class="speech-text">Where contractors help each other avoid <span class="warn">torn kites</span> &amp; only work with the <span class="good">best clients!</span></p>
      <div class="character-art" role="img" aria-label="Illustration of two friendly contractors standing together"></div>
      <div class="wordmark"><span class="dot"></span>Torn Kite</div>
    </section>
  </main>
</body>
</html>
```